TKA Electricial Contracting Services

Hi guys, after a design for my small electrical company, have logo design files to be incorporated into the layout, the basic concept is electrical contracting services for residential, commercial, industrial & data services, image is clean clear and strong,

Card format is to have a nice clean logo on front,with maybe the Residential – commercial – industrial - data, followed with licensed & insured, followed by contact details on backside of the card.

Target Market(s)

Residential, commercial, industrial sectors.

Industry/Entity Type

Electrical

Contact Information for Business Card

TKA logo,
Residential – commercial – industrial - data
REC: 61372
Email: tka@poralink.net.au
Phone: 0458 203 719

Requirements
Must have
• Clean & strong design.
Nice to have
• If possible, I would like the logo colours inverted so the text is orange and the background is black on the front of the card, then the backside of the card be the reverse colour
Should not have
• No Sparks, lightning bolts,

```html
<!DOCTYPE html>
<html lang="en">
<head>
<meta charset="utf-8">
<title>TKA Electrical – Business Card</title>
<link rel="stylesheet" href="https://fonts.googleapis.com/css2?family=Exo+2:wght@400;500;700&display=swap">
<style>
  :root {
    --orange: #f47b20;
    --black: #0d0d0d;
    --white: #ffffff;
    --backdrop: #e9e4dc;
    --font: "Exo 2", sans-serif;
  }
  * { margin: 0; padding: 0; box-sizing: border-box; }
  html, body {
    width: 1200px; height: 800px; overflow: hidden;
    background: var(--backdrop);
    font-family: var(--font);
  }
  .stage { position: relative; width: 1200px; height: 800px; }

  .card {
    position: absolute; top: 241px;
    width: 520px; height: 318px;
    overflow: hidden;
    box-shadow: 0 6px 18px rgba(0,0,0,0.18);
  }

  /* Contact side */
  .card--contact { left: 60px; background: var(--orange); color: var(--white); }
  .card--contact .corner { position: absolute; inset: 0; }
  .services {
    position: absolute; left: 236px; top: 26px;
    list-style: none; font-size: 14px; line-height: 1.2; font-weight: 400;
  }
  .brand { position: absolute; font-weight: 700; line-height: 1; }
  .brand__mark { display: block; letter-spacing: 1px; }
  .brand__name { display: block; }
  .card--contact .brand--main { left: 34px; top: 108px; color: var(--white); }
  .card--contact .brand--main .brand__mark { font-size: 64px; }
  .card--contact .brand--main .brand__name { font-size: 16px; margin-top: 4px; }
  .card--contact .brand--small { right: 26px; top: 92px; color: var(--white); text-align: center; }
  .card--contact .brand--small .brand__mark { font-size: 22px; }
  .card--contact .brand--small .brand__name { font-size: 5px; margin-top: 1px; }
  .contacts {
    position: absolute; left: 36px; top: 218px;
    list-style: none; font-size: 20px; line-height: 1.35;
  }
  .contacts li { display: flex; align-items: center; gap: 6px; }
  .contacts .phone { font-size: 22px; }
  .contacts svg { width: 18px; height: 18px; flex: none; }

  /* Logo side */
  .card--logo { left: 620px; background: var(--black); color: var(--white); text-align: center; }
  .card--logo .brand--main {
    left: 0; right: 0; top: 74px; color: var(--orange);
  }
  .card--logo .brand--main .brand__mark { font-size: 84px; }
  .card--logo .brand--main .brand__name { font-size: 20px; margin-top: 4px; }
  .tagline {
    position: absolute; left: 0; right: 0; top: 216px;
    font-size: 16px; line-height: 1.3; font-weight: 400;
  }
</style>
</head>
<body>
<main class="stage">

  <section class="card card--contact" aria-label="Business card contact side">
    <svg class="corner" viewBox="0 0 520 318" aria-hidden="true">
      <polygon points="312,0 520,0 520,318" fill="var(--black)"/>
    </svg>

    <ul class="services">
      <li>Residential</li>
      <li>Commercial</li>
      <li>Industrial</li>
      <li>Data</li>
      <li>REC: 61372</li>
    </ul>

    <div class="brand brand--main">
      <span class="brand__mark">TKA</span>
      <span class="brand__name">Tyler Kane Electrical</span>
    </div>

    <div class="brand brand--small">
      <span class="brand__mark">TKA</span>
      <span class="brand__name">Tyler Kane Electrical</span>
    </div>

    <ul class="contacts">
      <li class="phone">
        <svg viewBox="0 0 24 24" aria-hidden="true"><path fill="currentColor" d="M6.6 10.8a15.1 15.1 0 0 0 6.6 6.6l2.2-2.2a1 1 0 0 1 1-.25 11.4 11.4 0 0 0 3.6.57 1 1 0 0 1 1 1V20a1 1 0 0 1-1 1A17 17 0 0 1 3 4a1 1 0 0 1 1-1h3.5a1 1 0 0 1 1 1c0 1.25.2 2.45.57 3.57a1 1 0 0 1-.25 1z"/></svg>
        0458 203 719
      </li>
      <li class="email">
        <svg viewBox="0 0 24 24" aria-hidden="true"><path fill="currentColor" d="M2 5h20v14H2z"/><path fill="none" stroke="var(--orange)" stroke-width="1.8" d="M2 5l10 8 10-8"/></svg>
        tka@poralink.net.au
      </li>
    </ul>
  </section>

  <section class="card card--logo" aria-label="Business card logo side">
    <div class="brand brand--main">
      <span class="brand__mark">TKA</span>
      <span class="brand__name">Tyler Kane Electrical</span>
    </div>
    <p class="tagline">Electrical contracting services for residential,<br>commercial, industrial &amp; data services.</p>
  </section>

</main>
</body>
</html>
```